Real Estate Flyer

I would like an A4 size flyer which has the same info 3 times and can be cut into three.
It will be used for letterbox drops for new listings (SELLING) and sold listings (SOLD). The flyer needs a heading (as above) and a space for a photo which is able to be changed for each new property. Needs to be blue, red and white. It also requires my photo, KLT logo, Marisse Thornbury logo and the following text:
"Are you considering selling? Call Marisse today for a complimentary market appraisal".
(KLT logo, Marisse Thornbury Sales Consultant logo and my photo can be found in uploaded files)
Industry/Entity Type
Real Estate
Look and feel

```html
<!DOCTYPE html>
<html lang="en">
<head>
<meta charset="utf-8">
<title>KLT Appraisal Flyer</title>
<link rel="stylesheet" href="https://fonts.googleapis.com/css2?family=Roboto+Condensed:wght@400;700&display=swap">
<style>
  :root{
    --navy:#0a2a7a;
    --blue:#1c4fc4;
    --blue-light:#4a82e6;
    --red:#d8121b;
    --red-dark:#a80c12;
    --red-light:#f0463c;
    --white:#ffffff;
    --yellow:#ffe21a;
    --ink:#2b2b2b;
  }
  html,body{margin:0;padding:0;overflow:hidden;background:#fff;}
  .flyer{width:857px;height:1200px;position:relative;font-family:"Roboto Condensed","Arial Narrow",sans-serif;}
  .slip{position:relative;width:857px;height:400px;overflow:hidden;
    background:linear-gradient(180deg,var(--red-light) 0%,var(--red) 50%,var(--red-dark) 100%);}
  .slip-heading{position:absolute;left:0;top:0;width:100%;height:86px;margin:0;
    color:var(--white);font-weight:700;font-size:52px;line-height:86px;text-align:center;letter-spacing:.5px;}
  .body-band{position:absolute;left:0;top:86px;width:100%;height:230px;
    background:linear-gradient(180deg,var(--navy) 0%,var(--blue) 40%,var(--blue-light) 100%);}
  .slip-swoosh{position:absolute;left:0;top:280px;width:100%;height:60px;}
  .brand-bar{position:absolute;left:323px;top:89px;width:197px;height:25px;
    background:var(--white);display:flex;align-items:center;justify-content:center;gap:8px;
    color:var(--navy);font-weight:700;font-size:19px;letter-spacing:2px;}
  .brand-bar .mark{width:11px;height:11px;background:var(--red);}
  .property-frame{position:absolute;left:29px;top:94px;width:277px;height:226px;
    background:var(--white);padding:5px;box-sizing:border-box;}
  .property-photo{width:100%;height:100%;background:linear-gradient(180deg,#8fb6e6 0%,#c9d9ec 45%,#7f9a6a 80%,#5f7d4c 100%);}
  .property-photo.empty{background:var(--white);}
  .offer-caption{position:absolute;left:40px;top:326px;margin:0;color:var(--white);font-weight:700;font-size:27px;line-height:34px;}
  .call-text{position:absolute;left:322px;top:118px;width:270px;margin:0;color:var(--white);font-weight:700;font-size:29px;line-height:34px;}
  .phone{position:absolute;left:322px;top:236px;margin:0;color:var(--yellow);font-weight:700;font-size:40px;line-height:46px;letter-spacing:.5px;}
  .agent-photo{position:absolute;left:604px;top:92px;width:225px;height:228px;
    background:linear-gradient(180deg,#e9e5e2 0%,#c9b9ad 50%,#2a2a2a 80%,#b3121a 100%);}
  .agent-card{position:absolute;left:617px;top:314px;width:234px;height:58px;background:var(--white);
    display:flex;align-items:center;gap:10px;padding:0 12px;box-sizing:border-box;}
  .agent-card .mark{width:24px;height:24px;background:var(--red);flex:none;}
  .agent-name{color:var(--ink);font-size:19px;line-height:21px;}
  .agent-role{color:var(--ink);font-size:11px;margin-top:1px;}
</style>
</head>
<body>
<main class="flyer">

  <section class="slip">
    <h1 class="slip-heading">Are you considering selling?</h1>
    <div class="body-band"></div>
    <svg class="slip-swoosh" viewBox="0 0 857 60" preserveAspectRatio="none" aria-hidden="true">
      <path d="M0 36 C280 10 560 10 857 30 L857 60 L0 60 Z" fill="#ffffff" opacity=".85"/>
      <path d="M0 44 C280 20 560 20 857 38 L857 60 L0 60 Z" fill="#d8121b"/>
    </svg>
    <div class="brand-bar"><span class="mark"></span>KLT</div>
    <div class="property-frame"><div class="property-photo" role="img" aria-label="Photo of the property currently for sale"></div></div>
    <p class="offer-caption">SELLING: Offer No. 324323</p>
    <p class="call-text">Call Marisse today<br>for a complimentary<br>market appraisal.</p>
    <p class="phone">0400 555 218</p>
    <div class="agent-photo" role="img" aria-label="Portrait of sales consultant Marisse Thornbury"></div>
    <div class="agent-card"><span class="mark"></span><div><div class="agent-name">Marisse Thornbury</div><div class="agent-role">Sales Consultant</div></div></div>
  </section>

  <section class="slip">
    <h1 class="slip-heading">Are you considering selling?</h1>
    <div class="body-band"></div>
    <svg class="slip-swoosh" viewBox="0 0 857 60" preserveAspectRatio="none" aria-hidden="true">
      <path d="M0 36 C280 10 560 10 857 30 L857 60 L0 60 Z" fill="#ffffff" opacity=".85"/>
      <path d="M0 44 C280 20 560 20 857 38 L857 60 L0 60 Z" fill="#d8121b"/>
    </svg>
    <div class="brand-bar"><span class="mark"></span>KLT</div>
    <div class="property-frame"><div class="property-photo" role="img" aria-label="Photo of the recently sold property"></div></div>
    <p class="offer-caption">SOLD: Offer No. 324323</p>
    <p class="call-text">Call Marisse today<br>for a complimentary<br>market appraisal.</p>
    <p class="phone">0400 555 218</p>
    <div class="agent-photo" role="img" aria-label="Portrait of sales consultant Marisse Thornbury"></div>
    <div class="agent-card"><span class="mark"></span><div><div class="agent-name">Marisse Thornbury</div><div class="agent-role">Sales Consultant</div></div></div>
  </section>

  <section class="slip">
    <h1 class="slip-heading">Are you considering selling?</h1>
    <div class="body-band"></div>
    <svg class="slip-swoosh" viewBox="0 0 857 60" preserveAspectRatio="none" aria-hidden="true">
      <path d="M0 36 C280 10 560 10 857 30 L857 60 L0 60 Z" fill="#ffffff" opacity=".85"/>
      <path d="M0 44 C280 20 560 20 857 38 L857 60 L0 60 Z" fill="#d8121b"/>
    </svg>
    <div class="brand-bar"><span class="mark"></span>KLT</div>
    <div class="property-frame"><div class="property-photo empty" role="img" aria-label="Space for a property photo"></div></div>
    <p class="offer-caption">SOLD: Offer No. 324323</p>
    <p class="call-text">Call Marisse today<br>for a complimentary<br>market appraisal.</p>
    <p class="phone">0400 555 218</p>
    <div class="agent-photo" role="img" aria-label="Portrait of sales consultant Marisse Thornbury"></div>
    <div class="agent-card"><span class="mark"></span><div><div class="agent-name">Marisse Thornbury</div><div class="agent-role">Sales Consultant</div></div></div>
  </section>

</main>
</body>
</html>
```